Web page for a garment manufacturing company

We are clothing manufacturer based in Romania.
With our recent expansion, we have significantly increased our internal capacity, allowing us to take on new partnerships and deliver high-quality production services.
Our expertise includes producing classic coats, blazers, trousers, skirts, dresses, and blouses, though we are flexible and open to working with various other textile products.

Target Market(s)

High-end market and luxury

Industry/Entity Type

Garments Manufacturer

Coding

Coded - Design and coding required

Number of Pages Required

1 page

Colors

Designer to choose only greyscale colors for use in the design.

Requirements
Must have
• Velmora logo from our presentation
Nice to have
• https://www.dorlaque.pt/
Should not have
• prices, wedding dresses, collections

```html
<!DOCTYPE html>
<html lang="en">
<head>
<meta charset="UTF-8">
<title>Velmora – Garment Manufacturing</title>
<link href="https://fonts.googleapis.com/css2?family=Poppins:wght@300;400;500;600;700&display=swap" rel="stylesheet">
<style>
:root{
  --charcoal:#2a2a2a;
  --charcoal-dark:#1f1f1f;
  --accent:#5c5c5c;
  --accent-soft:#bdbdbd;
  --ink:#1d1d1d;
  --text:#3a3a3a;
  --light:#f5f5f5;
  --white:#ffffff;
  --line:#d9d9d9;
  --tint-1:#ececec;
  --tint-2:#f2f2f2;
  --tint-3:#e6e6e6;
}
*{margin:0;padding:0;box-sizing:border-box}
html,body{width:1200px;height:4619px;overflow:hidden}
body{font-family:'Poppins',sans-serif;color:var(--text);background:var(--white);position:relative}
.abs{position:absolute}
a{color:inherit;text-decoration:none}

/* top bar */
.topbar{left:0;top:0;width:1200px;height:50px;background:var(--accent);font-size:14px;color:var(--white)}
.topbar-left{left:0;top:0;width:510px;height:50px;background:var(--charcoal);clip-path:polygon(0 0,100% 0,94% 100%,0 100%)}
.topbar .item{top:15px;display:flex;align-items:center;gap:7px}

/* nav */
.nav{left:0;top:50px;width:1200px;height:86px;background:var(--white);border-bottom:1px solid #ececec}
.logo{left:127px;top:20px;font-size:38px;font-weight:400;color:var(--charcoal);letter-spacing:.5px}
.menu{right:127px;top:34px;display:flex;gap:38px;font-size:15px;color:var(--charcoal)}
.menu .active{color:#8a8a8a}

/* hero */
.hero{left:0;top:136px;width:1200px;height:589px;background:linear-gradient(135deg,#5a5a5a,#3a3a3a 55%,#4a4a4a)}
.hero h1{left:127px;top:150px;font-size:50px;font-weight:400;color:var(--white)}
.hero p{left:127px;top:236px;width:460px;font-size:24px;line-height:28px;color:var(--white)}
.btn{display:inline-flex;align-items:center;justify-content:center;background:var(--accent);color:var(--white);font-weight:600;border-radius:6px}
.hero .btn{left:127px;top:348px;width:158px;height:52px;font-size:16px;background:var(--white);color:var(--charcoal)}
.quote{left:689px;top:106px;width:384px;height:343px;background:var(--white);border-radius:14px}
.quote h3{left:0;top:40px;width:100%;text-align:center;font-size:18px;font-weight:600;color:var(--charcoal)}
.field{left:32px;width:320px;height:55px;border:1px solid var(--line);border-radius:6px;font-size:14px;color:#999;padding:17px 12px}
.quote .btn{left:32px;top:233px;width:320px;height:56px;font-size:16px;background:var(--charcoal)}

/* expertises */
.expertise{left:0;top:725px;width:1200px;height:725px;background:var(--light)}
.section-title{width:100%;text-align:center;font-size:42px;font-weight:400;color:var(--ink)}
.exp-card{width:183px;height:220px;background:var(--white);border-radius:10px;box-shadow:0 2px 10px rgba(0,0,0,.06)}
.exp-icon{left:46px;top:28px;width:90px;height:110px;border-radius:8px;background:linear-gradient(#eeeeee,#e2e2e2)}
.exp-label{left:10px;top:164px;width:163px;height:46px;border-radius:8px;display:flex;align-items:center;justify-content:center;font-size:14px;font-weight:600;color:var(--ink);letter-spacing:.5px}

/* about */
.about-frame{left:108px;top:1588px;width:230px;height:180px;background:var(--accent);border-radius:14px 60px 0 0}
.about-photo{left:127px;top:1604px;width:420px;height:429px;border-radius:10px;background:linear-gradient(160deg,#7c7c7c,#b4b4b4 40%,#666 75%,#3e3e3e)}
.about h2{left:608px;top:1600px;font-size:44px;font-weight:400;color:var(--ink)}
.about h2 span{color:#6a6a6a}
.about p{left:608px;width:466px;font-size:14.5px;line-height:21px;color:var(--text)}
.about .btn{left:608px;top:1963px;width:158px;height:56px;font-size:16px}
.grey-band{left:0;top:2153px;width:1200px;height:798px;background:var(--light)}
.stat{top:2072px;width:196px;height:171px;background:var(--white);border-radius:10px;box-shadow:0 2px 14px rgba(0,0,0,.07);text-align:center}
.stat .label{margin-top:44px;font-size:19px;line-height:24px;color:var(--ink)}
.stat .value{margin-top:12px;font-size:34px;font-weight:700;color:var(--ink)}

/* mission */
.mv h2{left:127px;font-size:44px;font-weight:400;color:var(--ink)}
.mv p{left:127px;width:460px;font-size:14.5px;line-height:21px;color:var(--text)}
.mission-photo{left:619px;top:2343px;width:454px;height:472px;border-radius:16px;background:linear-gradient(180deg,#8e8e8e,#6c6c6c 45%,#404040)}

/* services */
.svc{width:217px;height:241px;border-radius:10px;overflow:hidden}
.svc .ph{left:0;top:0;width:100%;height:100%}
.svc .name{left:0;bottom:22px;width:100%;text-align:center;font-size:18px;line-height:21px;color:var(--white);font-weight:500}

/* cta */
.cta{left:0;top:4013px;width:1200px;height:176px;background:var(--charcoal)}
.cta-band{left:0;top:0;width:918px;height:176px;background:var(--accent);clip-path:polygon(0 0,845px 0,918px 100%,0 100%)}
.cta h3{left:127px;top:55px;font-size:30px;line-height:42px;font-weight:700;color:var(--white)}
.cta .btn{left:630px;top:58px;width:188px;height:60px;background:var(--charcoal);font-size:19px;border-radius:10px}

/* footer */
.footer{left:0;top:4189px;width:1200px;height:430px;background:var(--charcoal)}
.footer h4{top:72px;font-size:18px;font-weight:600;color:var(--accent-soft)}
.footer ul{list-style:none;top:125px;font-size:14.5px;line-height:29px;color:var(--white)}
.footer .contact{left:484px;top:127px;font-size:14.5px;line-height:18px;color:var(--white)}
.footer .news{left:797px;top:127px;width:280px;font-size:14.5px;line-height:18px;color:var(--white)}
.footer .field{left:797px;top:213px;width:275px;height:46px;background:var(--white);border-radius:23px;padding:13px 18px;border:none}
.footer .btn{left:797px;top:271px;width:275px;height:46px;border-radius:23px;font-size:16px;background:#8a8a8a}
.footer .rule{left:116px;top:348px;width:980px;height:1px;background:rgba(255,255,255,.25)}
.social{top:378px;width:20px;height:20px;border-radius:50%;background:var(--white)}
.copy{right:127px;top:378px;font-size:14.5px;color:var(--white)}
</style>
</head>
<body>

<header class="abs topbar">
  <div class="abs topbar-left"></div>
  <div class="abs item" style="left:127px">
    <svg width="12" height="16" viewBox="0 0 12 16"><path d="M6 0a6 6 0 0 0-6 6c0 4.5 6 10 6 10s6-5.5 6-10a6 6 0 0 0-6-6zm0 8.5A2.5 2.5 0 1 1 6 3.5a2.5 2.5 0 0 1 0 5z" fill="#bdbdbd"/></svg>
    You can reach us on: ROMANIA
  </div>
  <div class="abs item" style="left:593px">
    <svg width="15" height="15" viewBox="0 0 24 24"><path d="M6.6 10.8a15 15 0 0 0 6.6 6.6l2.2-2.2c.3-.3.7-.4 1-.2 1.1.4 2.3.6 3.6.6.6 0 1 .4 1 1V20c0 .6-.4 1-1 1A17 17 0 0 1 3 4c0-.6.4-1 1-1h3.5c.6 0 1 .4 1 1 0 1.3.2 2.5.6 3.6.1.3 0 .7-.2 1z" fill="#fff"/></svg>
    Phone +40 300 555 012
  </div>
  <div class="abs item" style="left:812px">
    <svg width="16" height="13" viewBox="0 0 16 13"><rect width="16" height="13" rx="1.5" fill="#fff"/><path d="M1 1.5l7 5.5 7-5.5" stroke="#5c5c5c" stroke-width="1.4" fill="none"/></svg>
    Email: info@velmorafashion.com
  </div>
</header>

<nav class="abs nav">
  <div class="abs logo">Velmora</div>
  <div class="abs menu">
    <a class="active">Home</a><a>Manufacturing</a><a>Garment&nbsp; Solutions</a><a>Services</a><a>About Us</a><a>Contact Us</a>
  </div>
</nav>

<section class="abs hero">
  <div class="abs" role="img" aria-label="Aerial view of the factory buildings in grey tones" style="left:0;top:0;width:100%;height:100%;background:linear-gradient(160deg,rgba(120,120,120,.3),rgba(40,40,40,.25))"></div>
  <h1 class="abs">Welcome to Velmora</h1>
  <p class="abs">Established in 2005 as a Joint Venture between a local manufacturer and a foreign investor.</p>
  <a class="abs btn">READ MORE</a>
  <form class="abs quote">
    <h3 class="abs">GET A FREE QUOTE NOW</h3>
    <div class="abs field" style="top:93px">Name:</div>
    <div class="abs field" style="top:163px">Your Email id:</div>
    <a class="abs btn">GET QUOTE NOW</a>
  </form>
</section>

<section class="abs expertise">
  <h2 class="abs section-title" style="left:0;top:60px">Our Expertises</h2>
  <div class="abs exp-card" style="left:188px;top:154px"><div class="abs exp-icon" role="img" aria-label="Classic coat line icon"></div><div class="abs exp-label" style="background:var(--tint-1)">CLASSIC COATS</div></div>
  <div class="abs exp-card" style="left:396px;top:154px"><div class="abs exp-icon" role="img" aria-label="Blazer line icon"></div><div class="abs exp-label" style="background:var(--tint-2)">BLAZERS</div></div>
  <div class="abs exp-card" style="left:604px;top:154px"><div class="abs exp-icon" role="img" aria-label="Trousers line icon"></div><div class="abs exp-label" style="background:var(--tint-3)">TROUSERS</div></div>
  <div class="abs exp-card" style="left:812px;top:154px"><div class="abs exp-icon" role="img" aria-label="Skirt line icon"></div><div class="abs exp-label" style="background:var(--tint-1)">SKIRTS</div></div>
  <div class="abs exp-card" style="left:188px;top:402px"><div class="abs exp-icon" role="img" aria-label="Dress line icon"></div><div class="abs exp-label" style="background:var(--tint-3)">DRESSES</div></div>
  <div class="abs exp-card" style="left:396px;top:402px"><div class="abs exp-icon" role="img" aria-label="Blouse line icon"></div><div class="abs exp-label" style="background:var(--tint-1)">BLOUSES</div></div>
  <div class="abs exp-card" style="left:604px;top:402px"><div class="abs exp-icon" role="img" aria-label="Shirt line icon"></div><div class="abs exp-label" style="background:var(--tint-2)">SHIRTS</div></div>
  <div class="abs exp-card" style="left:812px;top:402px"><div class="abs exp-icon" role="img" aria-label="Gown line icon"></div><div class="abs exp-label" style="background:var(--tint-3)">MORE</div></div>
</section>

<div class="abs grey-band"></div>

<section class="about">
  <div class="abs about-frame"></div>
  <div class="abs about-photo" role="img" aria-label="Two workers reviewing garment samples at a table in the studio"></div>
  <h2 class="abs">About <span>Velmora</span></h2>
  <p class="abs" style="top:1673px"><strong style="color:var(--ink)">VELMORA</strong> is a manufacturing company for Ready-to-wear, situated in&nbsp; Focsani, a city with a rich tradition in the clothing industry. The top management is international, and we are proud to have a diverse and dynamic group of professionals from different countries working together.</p>
  <p class="abs" style="top:1802px">With our optimistic team spirit and passion for high-quality productions, we are ready to take on new challenges and delight our clients with very good results.</p>
  <p class="abs" style="top:1884px">In different specialized workshops making woven garments, knitting, leather goods, bags, leather accessories, bed linen, being always open to new projects and challenges.</p>
  <a class="abs btn">READ MORE</a>
  <div class="abs stat" style="left:605px"><div class="label">Ladie’s<br>Garments</div><div class="value">75%</div></div>
  <div class="abs stat" style="left:832px"><div class="label">Men’s<br>Garments</div><div class="value">25%</div></div>
</section>

<section class="mv">
  <h2 class="abs" style="top:2345px">Mission</h2>
  <p class="abs" style="top:2410px">To provide exceptional quality products and services, to meet our customers' expectations while being environmentally and socially responsible in every aspect of our business. Additionally, we recognize and value the importance of our workers, ensuring their well-being and fostering a positive and inclusive work environment.</p>
  <h2 class="abs" style="top:2577px">Vision</h2>
  <p class="abs" style="top:2641px">To be the leading destination for fashion brands who value both quality and sustainability. By prioritizing the well-being and satisfaction of our workers, we strive to create an environment that fosters innovation, collaboration, and growth, reinforcing our commitment to excellence and sustainable practices.</p>
  <div class="abs mission-photo" role="img" aria-label="Rack of grey knitwear on hangers"></div>
</section>

<section class="services">
  <h2 class="abs section-title" style="left:0;top:3032px">Our Services</h2>
  <div class="abs svc" style="left:127px;top:3118px"><div class="abs ph" role="img" aria-label="Show room with garments on rails" style="background:linear-gradient(180deg,#7a7a7a,#555 60%,#2e2e2e)"></div><div class="abs name">Show Room</div></div>
  <div class="abs svc" style="left:370px;top:3118px"><div class="abs ph" role="img" aria-label="Merchandising office with computers" style="background:linear-gradient(180deg,#929292,#575757 60%,#2c2c2c)"></div><div class="abs name">Merchandisers</div></div>
  <div class="abs svc" style="left:613px;top:3118px"><div class="abs ph" role="img" aria-label="Pattern construction workstation with CAD screen" style="background:linear-gradient(180deg,#cdcdcd,#7a7a7a 60%,#383838)"></div><div class="abs name">Pattern<br>Construction,<br>3D, CAD</div></div>
  <div class="abs svc" style="left:856px;top:3118px"><div class="abs ph" role="img" aria-label="Warehouse building exterior" style="background:linear-gradient(180deg,#c4c4c4,#6a6a6a 45%,#333)"></div><div class="abs name">Warehouse</div></div>
  <div class="abs svc" style="left:127px;top:3391px"><div class="abs ph" role="img" aria-label="Laboratory testing equipment" style="background:linear-gradient(180deg,#d6d6d6,#8b8b8b 55%,#303030)"></div><div class="abs name">Laboratory</div></div>
  <div class="abs svc" style="left:370px;top:3391px"><div class="abs ph" role="img" aria-label="Cutting room with long tables" style="background:linear-gradient(180deg,#dcdcdc,#8f8f8f 55%,#363636)"></div><div class="abs name">Cutting Room</div></div>
  <div class="abs svc" style="left:613px;top:3391px"><div class="abs ph" role="img" aria-label="Sewing section with machinists" style="background:linear-gradient(180deg,#a0a0a0,#6b6b6b 55%,#2d2d2d)"></div><div class="abs name">Sewing Section</div></div>
  <div class="abs svc" style="left:856px;top:3391px"><div class="abs ph" role="img" aria-label="Finishing area with hanging garments" style="background:linear-gradient(180deg,#a8a8a8,#707070 55%,#333)"></div><div class="abs name">Finishing</div></div>
  <div class="abs svc" style="left:370px;top:3662px"><div class="abs ph" role="img" aria-label="Quality control inspection of a garment" style="background:linear-gradient(180deg,#c6c6c6,#6e6e6e 55%,#2c2c2c)"></div><div class="abs name">Quality Control</div></div>
  <div class="abs svc" style="left:613px;top:3662px"><div class="abs ph" role="img" aria-label="Labeling and packing area with bagged garments" style="background:linear-gradient(180deg,#d9d9d9,#8a8a8a 55%,#353535)"></div><div class="abs name">Labeling, Packing</div></div>
</section>

<section class="abs cta">
  <div class="abs cta-band"></div>
  <h3 class="abs">Lorem ipsum dolor sit amet<br>consectetur adipiscing.</h3>
  <a class="abs btn">CONTACT US</a>
</section>

<footer class="abs footer">
  <h4 class="abs" style="left:126px">LINKS</h4>
  <ul class="abs" style="left:126px"><li>Home</li><li>About Us</li><li>Services</li><li>Blog</li><li>Gallery</li></ul>
  <h4 class="abs" style="left:283px">EXPERTISE</h4>
  <ul class="abs" style="left:283px"><li>Classic coats</li><li>Blazers</li><li>Trousers</li><li>Skirts</li><li>Dresses</li><li>Blouses</li></ul>
  <h4 class="abs" style="left:484px">CONTACT</h4>
  <div class="abs contact">ROMANIA<br>Focsani&nbsp; Bd. Unirii 48,<br>Zip code: 620450<br><br>Phone +40 300 555 012<br><br>Fax +40 300 555 018<br><br>Email: info@velmorafashion.com</div>
  <h4 class="abs" style="left:797px">JOIN OUR NEWSLETER</h4>
  <div class="abs news">Lorem ipsum dolor sit amet, clorons ectetur adipiscing elit, sed do elius mod tempor incididunt.</div>
  <div class="abs field">Name:</div>
  <a class="abs btn">SIGN UP</a>
  <div class="abs rule"></div>
  <span class="abs social" style="left:126px" aria-label="Social profile"></span>
  <span class="abs social" style="left:166px" aria-label="Social profile"></span>
  <span class="abs social" style="left:206px" aria-label="Social profile"></span>
  <div class="abs copy">Copyright © 2024 All rights are reserved.</div>
</footer>

</body>
</html>
```